I would like an amazing design for a eCommerce website called trailhaven.net.

The logo was designed on SketchHive and is attached below. Whatever your design - it MUST use this logo. Please don't waste your time designing new logos.

The logo is on both black and white backgrounds as I've not yet made my mind up whether to ditch "cool black" in favour of more "fresh, clean white"! I'd like to look at both options.

Trail Haven is going to be the first destination of choice for anyone who is bored or frustrated at home and wants a life full of adventure. It will stock outdoor clothing and equipment, training kit, expedition gear, and travel clothing and accessories.

But it is a very cool place to go. A fun and exciting Aladdin's cave full of fantastic adventure kit. We will stock inflatable pack rafts, machetes, hammocks and other expedition gear as well as standard outdoor clothing.

This is NOT a geeky outdoor store selling pac-a-macs and walking poles.

The unique thing is that everything stocked is hand selected by me, Tom Bexley, an experienced explorer who became the first person to walk the Amazon in 2010. tombexley.net is my site. I now make TV for Horizon Network.

There will be items at every price level from "only the best" - absolute top end kit, to "get the job done" - stuff that won't break the bank. Everything stocked works. If it doesn't - I won't sell it.

So although the theme is fun and adventurous I have to have it also feeling like a place of professional, expert advice. A place of substance and depth.

Thanks in advance for all your ideas and designs!

Best
Tom
Updates

The designs that I like the best have used jungle images as background wallpaper - possible with a green tint to them so that they really do look like background rather than the focus. The focus should obviously be the kit for sale. The best designs have this on a fresh white or light grey background so that it stands out. I like the main logo being in a black header and footer. But the feel of the site can easily become too dark if too much back is used or if the green background image is too dark. We want adventure and cool - but it has to feel light and professional enough to be accessible by people of all ages. Most websites that are successful are white after all and whilst I'd like to be a bit more adventurous than that we shouldn't over do the darkness!

I'm not really a massive fan of side bars and would hope that whichever site I chose had a mega menu system like Corwin Latch that could navigate quickly and easily to any item intuitively.

Any sliders must be about selling kit not images of me.

Thanks so much to everyone who has submitted designs - there are some VERY cool ones out there at the moment

Best,
Tom

Target Market(s)

The target market is primarily 16 to 50 years old outdoor enthusiasts however I will be selling to older people and kids, male and female, so it can't be too modern, too macho, or too complicated to put anyone off.

Requirements
Must have
• Bold, professional, adventurous feel. Not cluttered but not so minimalist that it looks boring too. I would like to select a few colours and work with them.
• Red for high lighted emphasis. See logo
• Greens/blacks/greys as background.
• Clean menu system. I'm probably going use a tailored version of http://plumtide-theme.shopsample.net with mega menus.
Nice to have
• Some personalisation that makes the site mine. Use of hi res images below as background could work although I am keen for the site to look clean and easy to navigate.
Should not have
• Hundreds of boxes and text and clutter. I want this site to show off the items in a classy manner. This is NOT gear barn.net! This is a site where hand selected items are proudly displayed and put together, after a lot of thought.

```html
<!DOCTYPE html>
<html lang="en">
<head>
<meta charset="utf-8">
<title>Trail Haven – Everything for a life of adventure</title>
<link href="https://fonts.googleapis.com/css2?family=Archivo:ital,wght@0,400;0,700;0,900;1,400;1,700&display=swap" rel="stylesheet">
<style>
:root{
  --black:#000;
  --ink:#111;
  --bar-top:#3a3a3a;
  --bar-bottom:#0d0d0d;
  --band:#2a2a2a;
  --light:#f2f2f2;
  --panel:#d9dbd7;
  --white:#fff;
  --red:#c8161d;
  --gold:#b59a18;
  --muted:#8a8a8a;
  --field:#e9e9e9;
}
*{box-sizing:border-box;margin:0;padding:0}
html,body{width:840px;height:1200px;overflow:hidden;background:var(--white)}
body{font-family:"Archivo",Arial,sans-serif;color:var(--ink);position:relative}
.abs{position:absolute}

/* header */
.site-header{position:absolute;left:0;top:0;width:840px;height:80px;background:var(--white)}
.brand{position:absolute;left:69px;top:28px}
.brand-name{font-weight:900;font-size:27px;letter-spacing:1px;line-height:1;color:var(--black);text-transform:uppercase}
.brand-tag{font-size:10.5px;font-weight:700;color:var(--black);margin-top:2px}
.account{position:absolute;left:600px;top:17px;font-size:11px;color:var(--ink)}
.account .or{color:var(--red)}
.cart{position:absolute;left:684px;top:7px}
.cart-pill{position:absolute;left:690px;top:17px;width:78px;height:22px;border-radius:11px;background:#3c3c3c;color:var(--white);font-size:9px;line-height:22px;padding-left:41px}

/* nav */
.main-nav{position:absolute;left:0;top:80px;width:840px;height:29px;background:linear-gradient(var(--bar-top),var(--bar-bottom))}
.main-nav ul{list-style:none;display:flex;position:absolute;left:91px;top:0;height:29px}
.main-nav li{font-size:10px;color:var(--white);line-height:29px;padding:0 11px;border-right:1px solid #4a4a4a;text-transform:uppercase}
.main-nav li.active{color:var(--gold)}
.main-nav li:last-child{border-right:none}
.search-label{position:absolute;left:600px;top:0;line-height:29px;font-size:10px;color:var(--white)}
.search-field{position:absolute;left:649px;top:5px;width:118px;height:18px;background:var(--white);border-radius:9px}

/* slider */
.hero{position:absolute;left:0;top:109px;width:840px;height:262px;background:var(--light)}
.hero-frame{position:absolute;left:148px;top:18px;width:532px;height:220px;border-radius:8px;background:#e4e4e4;box-shadow:0 6px 10px rgba(0,0,0,.25);padding:4px}
.hero-photo{width:100%;height:100%;border-radius:6px;background:linear-gradient(160deg,#5c6a3a,#2f3a22 45%,#6b7450 70%,#8d9a8a)}
.hero-arrow{position:absolute;top:100px;width:34px;height:34px;border-radius:50%;background:radial-gradient(#fafafa,#cfcfcf);box-shadow:0 1px 3px rgba(0,0,0,.35)}
.hero-arrow.prev{left:128px}
.hero-arrow.next{left:669px}

/* categories */
.category{position:absolute;top:380px;width:180px;height:110px}
.category-icon{position:absolute;top:0}
.category-label{position:absolute;left:0;top:66px;font-size:11.5px;line-height:13px;text-transform:uppercase;color:var(--ink)}
.category.active .category-label{color:var(--gold)}
.category-tick{position:absolute;left:83px;top:498px;width:146px;height:5px;background:var(--red)}
.category-caret{position:absolute;left:150px;top:503px;border:5px solid transparent;border-top-color:var(--red)}
.category-rule{position:absolute;left:69px;top:511px;width:702px;height:3px;background:var(--red)}

/* products */
.products{position:absolute;left:69px;top:514px;width:702px;height:377px;background:linear-gradient(120deg,#cfd2cc,#e3e4e1 40%,#d3d5d0 70%,#e6e6e4)}
.product{position:absolute;width:190px;text-align:center}
.product-photo{width:190px;height:106px;border-radius:95px 95px 0 0;border:3px solid var(--white);border-bottom:none;box-shadow:0 -1px 3px rgba(0,0,0,.2)}
.product-text{font-size:7px;font-weight:700;font-style:italic;line-height:10px;margin-top:7px;text-transform:uppercase}
.quick-view{display:inline-block;margin-top:5px;width:90px;height:20px;border-radius:10px;background:var(--black);color:var(--white);font-size:9px;font-weight:700;line-height:20px}

/* payments */
.payments{position:absolute;left:0;top:904px;width:840px;height:51px;background:var(--band)}
.payments-title{position:absolute;left:69px;top:0;width:175px;height:51px;background:var(--white);font-weight:700;font-size:16px;line-height:51px;padding-left:37px}
.card{position:absolute;top:8px;height:36px;background:var(--white);border:2px solid #bbb;font-size:11px;font-weight:700;color:#333;text-align:center;line-height:32px}

/* footer */
.site-footer{position:absolute;left:0;top:955px;width:840px;height:245px;background:var(--black);color:var(--white)}
.subscribe-title{position:absolute;left:108px;top:18px;font-weight:700;font-size:12.5px;line-height:18px;text-transform:uppercase}
.newsletter{position:absolute;left:244px;top:14px;width:433px;height:71px;background:var(--band)}
.newsletter p{position:absolute;left:34px;top:8px;font-size:10px}
.email-field{position:absolute;left:22px;top:28px;width:321px;height:32px;border-radius:16px;background:var(--field);color:#9a9a9a;font-size:10px;font-weight:700;font-style:italic;line-height:32px;padding-left:50px}
.go{position:absolute;left:359px;top:27px;width:36px;height:36px;border-radius:50%;background:radial-gradient(#555,#111);font-weight:700;font-size:13px;line-height:36px;text-align:center}
.footer-col{position:absolute;top:103px}
.footer-col h3{font-size:10px;font-weight:700;font-style:italic;text-decoration:underline;margin-bottom:12px}
.quick-links li{list-style:none;font-size:6.5px;line-height:10.5px;text-transform:uppercase}
.social li{list-style:none;font-size:10px;font-style:italic;color:#aaa;line-height:21px;display:flex;align-items:center;gap:7px}
.social .dot{width:10px;height:10px;background:#777;display:inline-block}
.contact li{list-style:none;font-size:13px;line-height:26px;display:flex;align-items:center;gap:8px}
.contact li.mail{font-size:10px}
.footer-brand{position:absolute;left:580px;top:196px;color:var(--white)}
.footer-brand .brand-name{color:var(--white);font-size:18px}
.footer-brand .brand-tag{color:var(--white);font-size:7px}
.copyright{position:absolute;left:404px;top:217px;font-size:6.5px}
</style>
</head>
<body>

<header class="site-header">
  <div class="brand">
    <div class="brand-name">Trail Haven</div>
    <div class="brand-tag">Everything for a life of adventure - by Tom Bexley</div>
  </div>
  <div class="account">Log in <span class="or">or</span> Sign up</div>
  <span class="cart-pill">View Cart</span>
  <svg class="cart" width="44" height="44" viewBox="0 0 44 44">
    <circle cx="22" cy="22" r="21" fill="#555" stroke="#bbb" stroke-width="1.5"/>
    <path d="M11 16h4l3 11h11l3-8H17" fill="none" stroke="#fff" stroke-width="1.8"/>
    <circle cx="19" cy="30" r="1.8" fill="#fff"/><circle cx="28" cy="30" r="1.8" fill="#fff"/>
  </svg>
</header>

<nav class="main-nav">
  <ul>
    <li class="active">Home</li><li>Shop</li><li>Expeditions</li><li>DVD &amp; Book</li><li>Speaking</li><li>Blog</li><li>Contact</li>
  </ul>
  <span class="search-label">SEARCH</span>
  <div class="search-field">
    <svg width="118" height="18"><circle cx="103" cy="8" r="4" fill="none" stroke="#111" stroke-width="1.6"/><path d="M106 11l4 4" stroke="#111" stroke-width="1.8"/></svg>
  </div>
</nav>

<section class="hero">
  <div class="hero-frame"><div class="hero-photo" role="img" aria-label="Explorer wading through a flooded mangrove jungle holding a machete"></div></div>
  <svg class="hero-arrow prev" viewBox="0 0 34 34"><circle cx="17" cy="17" r="9" fill="#bbb"/><path d="M20 12l-6 5 6 5" fill="#fff"/></svg>
  <svg class="hero-arrow next" viewBox="0 0 34 34"><circle cx="17" cy="17" r="9" fill="#bbb"/><path d="M14 12l6 5-6 5" fill="#fff"/></svg>
</section>

<div class="category active" style="left:101px">
  <svg class="category-icon" style="left:44px" width="64" height="64" viewBox="0 0 70 70">
    <path d="M35 3a32 32 0 1 1-32 32" fill="none" stroke="#c8a615" stroke-width="3"/>
    <circle cx="38" cy="34" r="25" fill="none" stroke="#c8161d" stroke-width="6"/>
    <path d="M27 24l7-3h8l7 3 3 8-5 1v15H29V33l-5-1z" fill="#c8161d"/>
  </svg>
  <div class="category-label">Outdoor<br>Clothing<br>and Equipment</div>
</div>
<div class="category" style="left:287px">
  <svg class="category-icon" style="left:39px" width="64" height="64" viewBox="0 0 70 70">
    <path d="M35 3a32 32 0 1 1-32 32" fill="none" stroke="#111" stroke-width="3"/>
    <circle cx="38" cy="34" r="25" fill="none" stroke="#111" stroke-width="6"/>
    <circle cx="36" cy="24" r="5" fill="#111"/><path d="M28 48l4-17h8l2 17z M24 36l8-4" fill="#111" stroke="#111" stroke-width="3"/>
  </svg>
  <div class="category-label">Training<br>Kit</div>
</div>
<div class="category" style="left:447px">
  <svg class="category-icon" style="left:46px" width="64" height="64" viewBox="0 0 70 70">
    <path d="M35 3a32 32 0 1 1-32 32" fill="none" stroke="#111" stroke-width="3"/>
    <circle cx="38" cy="34" r="25" fill="none" stroke="#111" stroke-width="6"/>
    <circle cx="34" cy="36" r="7" fill="none" stroke="#111" stroke-width="5"/>
    <circle cx="45" cy="25" r="4" fill="none" stroke="#111" stroke-width="3"/>
  </svg>
  <div class="category-label">Expedition<br>Gear</div>
</div>
<div class="category" style="left:625px">
  <svg class="category-icon" style="left:38px" width="64" height="64" viewBox="0 0 70 70">
    <path d="M35 3a32 32 0 1 1-32 32" fill="none" stroke="#111" stroke-width="3"/>
    <circle cx="38" cy="34" r="25" fill="none" stroke="#111" stroke-width="6"/>
    <path d="M24 28l10 6-10 6z M52 28l-10 6 10 6z" fill="#111"/><rect x="34" y="31" width="8" height="6" fill="#111"/>
  </svg>
  <div class="category-label">Travel<br>Clothing<br>and Accessories</div>
</div>
<div class="category-tick"></div>
<div class="category-caret"></div>
<div class="category-rule"></div>

<section class="products" role="img" aria-label="Faint green-grey jungle wallpaper behind the product grid"></section>
<div class="product" style="left:92px;top:531px">
  <div class="product-photo" role="img" aria-label="Hiker with a large backpack in the forest" style="background:linear-gradient(#4d6a2e,#7c8f4a 60%,#3e5224)"></div>
  <p class="product-text">Lorem ipsum is simply dummy text of the<br>printing and typesetting industry.</p>
  <span class="quick-view">QUICK VIEW</span>
</div>
<div class="product" style="left:324px;top:531px">
  <div class="product-photo" role="img" aria-label="Family sledging in the snow" style="background:linear-gradient(#8fa9c4,#c9d9e8 55%,#f3f6f8)"></div>
  <p class="product-text">Lorem ipsum is simply dummy text of the<br>printing and typesetting industry.</p>
  <span class="quick-view">QUICK VIEW</span>
</div>
<div class="product" style="left:556px;top:531px">
  <div class="product-photo" role="img" aria-label="Climber's boots on a mossy rock" style="background:linear-gradient(#6f8b3a,#344523 60%,#55663a)"></div>
  <p class="product-text">Lorem ipsum is simply dummy text of the<br>printing and typesetting industry.</p>
  <span class="quick-view">QUICK VIEW</span>
</div>
<div class="product" style="left:92px;top:709px">
  <div class="product-photo" role="img" aria-label="Children in sun hats on a sandy beach" style="background:linear-gradient(#3f7fc4,#8fbbe2 50%,#d7b98a)"></div>
  <p class="product-text">Lorem ipsum is simply dummy text of the<br>printing and typesetting industry.</p>
  <span class="quick-view">QUICK VIEW</span>
</div>
<div class="product" style="left:324px;top:709px">
  <div class="product-photo" role="img" aria-label="Trekker in a cap with a backpack among trees" style="background:linear-gradient(#5b7a34,#8a9a5a 55%,#4a5a2c)"></div>
  <p class="product-text">Lorem ipsum is simply dummy text of the<br>printing and typesetting industry.</p>
  <span class="quick-view">QUICK VIEW</span>
</div>
<div class="product" style="left:556px;top:709px">
  <div class="product-photo" role="img" aria-label="Child skiing on a snowy slope" style="background:linear-gradient(#b9cfe6,#e8f0f7 55%,#f8fafc)"></div>
  <p class="product-text">Lorem ipsum is simply dummy text of the<br>printing and typesetting industry.</p>
  <span class="quick-view">QUICK VIEW</span>
</div>

<section class="payments">
  <div class="payments-title">WE ACCEPT</div>
  <div class="card" style="left:317px;width:60px">PayLoom</div>
  <div class="card" style="left:394px;width:60px">Rovera</div>
  <div class="card" style="left:470px;width:58px;font-size:8px">MeridianCard</div>
  <div class="card" style="left:543px;width:58px">VANTA</div>
  <div class="card" style="left:618px;width:59px;font-size:9px">Vanta Spark</div>
</section>

<footer class="site-footer">
  <div class="subscribe-title">Subscribe your<br>newsletters<br>today!</div>
  <div class="newsletter">
    <p>Sign up to our newsletter for the latest news and special offers.</p>
    <div class="email-field">ENTER YOUR EMAIL HERE</div>
    <div class="go">GO</div>
  </div>

  <div class="footer-col" style="left:261px">
    <h3>Quick Links</h3>
    <ul class="quick-links"><li>Home</li><li>Shop</li><li>Expeditions</li><li>DVD &amp; Book</li><li>Speaking</li><li>Blog</li><li>Contact</li></ul>
  </div>
  <div class="footer-col" style="left:403px">
    <h3>Connect With Us</h3>
    <ul class="social"><li><span class="dot"></span>Circlebook</li><li><span class="dot"></span>Chirper</li><li><span class="dot"></span>ViewTube</li></ul>
  </div>
  <div class="footer-col" style="left:531px">
    <h3>Contact Us</h3>
    <ul class="contact">
      <li><svg width="16" height="16" viewBox="0 0 16 16"><circle cx="8" cy="8" r="7" fill="none" stroke="#fff"/><path d="M5 4l2 2-1 1 3 3 1-1 2 2-2 1C7 11 5 9 4 6z" fill="#fff"/></svg>555-010-482</li>
      <li class="mail"><svg width="16" height="16" viewBox="0 0 16 16"><circle cx="8" cy="8" r="7" fill="none" stroke="#fff"/><rect x="4" y="5" width="8" height="6" fill="none" stroke="#fff"/><path d="M4 5l4 3 4-3" fill="none" stroke="#fff"/></svg>maya@mayalane.co.uk</li>
    </ul>
  </div>

  <div class="footer-brand">
    <div class="brand-name">Trail Haven</div>
    <div class="brand-tag">Everything for a life of adventure - by Tom Bexley</div>
  </div>
  <div class="copyright">copyright@trailhaven.net</div>
</footer>

</body>
</html>
```